KRL Banner Logo with Rocky Mountain of CO as the background

I need a banner/logo for my KRL year. So have a banner design that is like an intentional path or inspiring.

• KRL Silver Ridge CO mountain as background and they may add similar images that I sent you
• Wording: Intentional Path
Learning year 2025-2026
• Add the KRL logo (the white and blue image – you will see these online)

UPDATE: Attached are example images on how we envision the banner. Please do not use the attached example sample images. Kindly look for similar looking images that are FREE TO USE Commercially.

CEO, top executives

0054AA
0677BA
7BADD7
CADEEF
E8F1F8

• • KRL Silver Ridge CO mountain as background and they may add similar images that I sent you • Wording: Intentional Path Learning year 2025-2026 • Add the KRL logo (the white and blue image – you will see these online)
• It has nice to have the inspirational images attached but you can have your own design. This is only for sample.

```html
<!DOCTYPE html>
<html lang="en">
<head>
<meta charset="utf-8">
<title>Intentional Path – Learning year 2025-2026</title>
<link href="https://fonts.googleapis.com/css2?family=Roboto+Slab:wght@700&family=Montserrat:wght@600;700&display=swap" rel="stylesheet">
<style>
  :root {
    --navy-deep: #0b1a45;
    --blue-strong: #0054aa;
    --blue-mid: #0677ba;
    --blue-sky: #7badd7;
    --blue-title: #6fbdf0;
    --blue-pale: #cadeef;
    --blue-mist: #e8f1f8;
    --grey-wash: #dcdfe3;
    --white: #ffffff;
  }
  html, body {
    margin: 0;
    padding: 0;
    overflow: hidden;
    background: var(--white);
  }
  .banner {
    position: relative;
    width: 1200px;
    height: 326px;
    overflow: hidden;
    background: var(--white);
  }
  .banner__wash {
    position: absolute;
    inset: 0;
    width: 1200px;
    height: 326px;
  }
  .banner__scene {
    position: absolute;
    top: 0;
    right: 0;
    width: 640px;
    height: 326px;
  }
  .headline {
    position: absolute;
    left: 60px;
    top: 76px;
    width: 440px;
    margin: 0;
    text-align: center;
    font-family: "Roboto Slab", Georgia, serif;
    font-weight: 700;
    font-size: 42px;
    line-height: 1;
    color: var(--blue-title);
  }
  .year-band {
    position: absolute;
    left: 58px;
    top: 132px;
    width: 440px;
    height: 64px;
  }
  .year-band svg {
    position: absolute;
    inset: 0;
  }
  .year-band__text {
    position: relative;
    margin: 0;
    line-height: 64px;
    text-align: center;
    font-family: "Montserrat", Arial, sans-serif;
    font-weight: 700;
    font-size: 23px;
    color: var(--white);
  }
  .brand {
    position: absolute;
    left: 238px;
    top: 216px;
    display: flex;
    align-items: center;
    gap: 7px;
  }
  .brand__dot {
    width: 12px;
    height: 12px;
    border-radius: 50%;
    background: var(--navy-deep);
  }
  .brand__name {
    font-family: "Montserrat", Arial, sans-serif;
    font-weight: 600;
    font-size: 15px;
    letter-spacing: 0.5px;
    color: var(--navy-deep);
  }
</style>
</head>
<body>
  <div class="banner">
    <svg class="banner__wash" viewBox="0 0 1200 326" aria-hidden="true">
      <defs>
        <radialGradient id="wash-grey" cx="0.25" cy="0.5" r="0.6">
          <stop offset="0" stop-color="var(--grey-wash)" stop-opacity="0.35"/>
          <stop offset="1" stop-color="var(--grey-wash)" stop-opacity="0"/>
        </radialGradient>
      </defs>
      <rect width="1200" height="326" fill="url(#wash-grey)"/>
    </svg>

    <svg class="banner__scene" viewBox="0 0 640 326" aria-hidden="false">
      <defs>
        <linearGradient id="mountain-tones" x1="0" y1="0" x2="0.3" y2="1">
          <stop offset="0" stop-color="var(--blue-pale)"/>
          <stop offset="0.35" stop-color="var(--blue-sky)"/>
          <stop offset="0.65" stop-color="var(--blue-strong)"/>
          <stop offset="1" stop-color="var(--navy-deep)"/>
        </linearGradient>
      </defs>
      <path class="scene__accent" fill="var(--blue-sky)" opacity="0.55"
        d="M40 10 L120 0 L110 18 L60 22 Z M20 240 L90 230 L70 262 L10 268 Z M540 300 L640 290 L640 320 L560 326 Z M600 0 L640 0 L640 40 L620 30 Z"/>
      <path class="scene__accent" fill="var(--blue-pale)" opacity="0.8"
        d="M0 150 L40 140 L35 160 L5 168 Z M480 20 L560 8 L555 26 L470 32 Z"/>
      <path role="img" aria-label="Photo of rugged snow-dusted mountain peaks under a pale blue sky"
        fill="url(#mountain-tones)"
        d="M70 22 L140 12 L210 18 L300 6 L420 14 L520 4 L600 16 L640 10 L640 300 L600 292 L540 304 L470 296 L400 306 L320 294 L250 300 L190 288 L150 270 L120 250 L96 230 L80 200 L60 170 L70 140 L48 110 L62 80 L44 50 Z"/>
    </svg>

    <h1 class="headline">Intentional Path</h1>

    <div class="year-band">
      <svg viewBox="0 0 440 64" aria-hidden="true">
        <path fill="var(--navy-deep)"
          d="M14 6 L120 2 L260 6 L420 0 L436 10 L428 22 L440 34 L430 48 L436 58 L300 62 L160 60 L40 64 L4 58 L12 46 L0 32 L10 20 L2 10 Z"/>
      </svg>
      <p class="year-band__text">Learning year 2025-2026</p>
    </div>

    <div class="brand">
      <span class="brand__dot"></span>
      <span class="brand__name">KRL</span>
    </div>
  </div>
</body>
</html>
```